Expedition Cruise Sales Website for the Polar Regions (Antarctica & Arctic)

This will be a website for selling cruises.
This site should have a homepage, a ship page, destinations, and itineraries.
I have created a file specifying each page, and it is attached.
Pages:
1. Home
2. Cruise Lines
- 2.1 Ships
3. Destinations
- 3.1 Region - 3.2 Country - 3.3 City
4. Itineraries
- 4.1 Itinerary
5. Blog / Travel Tips 6. About Us
7. Contact
Please take a look on the attached pdf
Target Market(s)
Expedition Travelers
Coding
Coded - Design and coding required
Number of Pages Required
5+ page

```html
<!DOCTYPE html>
<html lang="en">
<head>
<meta charset="utf-8">
<title>Floeline.co – Expedition Cruises</title>
<link href="https://fonts.googleapis.com/css2?family=Lato:wght@400;700;900&display=swap" rel="stylesheet">
<style>
:root{
  --navy:#0e1c3b;
  --navy-2:#14284f;
  --blue:#2b62ad;
  --blue-light:#3f7fd0;
  --ink:#1b1f2a;
  --muted:#5c6270;
  --line:#e2e5ea;
  --field:#e9ebee;
  --white:#ffffff;
  --star:#f2b417;
  --green:#2fb34a;
}
*{box-sizing:border-box;margin:0;padding:0}
html,body{width:1200px;height:3744px;overflow:hidden}
body{font-family:"Lato",Arial,sans-serif;color:var(--ink);background:var(--white);position:relative}
.abs{position:absolute}

/* header / hero */
.hero{position:absolute;left:0;top:0;width:1200px;height:700px;
  background:linear-gradient(180deg,#143a5c 0%,#1f6f8c 38%,#2c8fa3 60%,#1b4c6a 100%)}
.hero-shade{position:absolute;inset:0;background:linear-gradient(90deg,rgba(10,25,50,.55) 0%,rgba(10,25,50,.15) 60%,rgba(10,25,50,0) 100%)}
.hero-ship{position:absolute;left:700px;top:250px;width:380px;height:260px;border-radius:30px;
  background:radial-gradient(ellipse at 50% 55%,#f4f6f8 0%,#cfd8e0 40%,rgba(40,110,140,0) 72%)}
.nav{position:absolute;top:0;left:0;width:1200px;height:64px}
.brand{position:absolute;left:112px;top:14px;font-size:30px;font-weight:900;color:var(--white);display:flex;align-items:center;gap:10px}
.brand .mark{width:30px;height:30px;border-radius:50%;background:var(--white)}
.nav-links{position:absolute;left:380px;top:24px;display:flex;gap:30px;font-size:14px;color:var(--white)}
.nav-links .active{font-weight:700;border-bottom:2px solid var(--white);padding-bottom:4px}
.nav-cta{position:absolute;left:905px;top:16px;width:178px;height:36px;background:var(--navy);color:var(--white);font-size:14px;font-weight:700;display:flex;align-items:center;justify-content:center;border-radius:2px}
.hero h1{position:absolute;left:112px;top:215px;font-size:46px;font-weight:700;color:var(--white)}
.hero p{position:absolute;left:112px;top:290px;width:500px;font-size:17px;line-height:1.5;color:var(--white)}
.search{position:absolute;left:112px;top:440px;display:flex;gap:14px}
.search .sel{width:160px;height:36px;background:var(--white);border-radius:2px;font-size:14px;color:var(--ink);padding:0 12px;display:flex;align-items:center;justify-content:space-between}
.btn{background:var(--blue);color:var(--white);font-weight:700;font-size:14px;display:flex;align-items:center;justify-content:center;border-radius:3px}
.hero .btn{position:absolute;left:112px;top:535px;width:140px;height:40px}
.play{position:absolute;left:925px;top:310px;width:76px;height:76px;border-radius:50%;background:var(--navy-2);border:4px solid rgba(255,255,255,.8)}
.dots{position:absolute;display:flex;gap:6px}
.dots i{display:block;width:18px;height:5px;border-radius:3px;background:rgba(255,255,255,.5)}
.dots i.on{background:var(--white)}

/* section titles */
.title{position:absolute;left:0;width:1200px;text-align:center;font-size:44px;font-weight:700;color:var(--ink)}
.title span{color:var(--blue)}
.sub{position:absolute;left:0;width:1200px;text-align:center;font-size:18px;color:var(--muted)}

/* offers */
.offer{position:absolute;top:895px;width:298px;height:418px;background:var(--white);border:1px solid var(--line);box-shadow:0 4px 14px rgba(0,0,0,.08);border-radius:4px;overflow:hidden;text-align:center}
.offer .img{height:210px;margin:8px;border-radius:3px}
.offer h3{font-size:19px;font-weight:700;margin-top:14px}
.offer p{font-size:13px;color:var(--muted);line-height:1.5;width:220px;margin:10px auto 0}
.offer .btn{width:128px;height:34px;margin:20px auto 0}
.arrow{position:absolute;width:32px;height:32px;border-radius:50%;background:var(--blue);display:flex;align-items:center;justify-content:center}

/* destinations */
.dest{position:absolute;left:0;top:1400px;width:1200px;height:510px;background:linear-gradient(180deg,#1a2c50 0%,#0e1c3b 100%)}
.dest .title{color:var(--white);top:60px}
.dest .sub{color:#dfe5ef;top:130px;width:560px;left:320px;line-height:1.5}
.dest-item{position:absolute;top:230px;width:240px;text-align:center;color:var(--white)}
.dest-item .ic{width:96px;height:96px;border-radius:50%;background:var(--blue-light);margin:0 auto;border:4px solid rgba(255,255,255,.25);display:flex;align-items:center;justify-content:center}
.dest-item h4{font-size:22px;font-weight:700;color:var(--blue-light);margin-top:26px}
.dest-item p{font-size:14px;line-height:1.5;margin-top:6px;color:#e4e9f2}

/* cruise lines */
.cl-title{position:absolute;left:112px;top:2015px;font-size:40px;font-weight:700}
.cl-title span{color:var(--blue)}
.cl-text{position:absolute;left:112px;top:2080px;width:300px;font-size:17px;line-height:1.5;color:var(--muted)}
.cl-card{position:absolute;top:2020px;height:280px;border-radius:4px}

/* testimonials */
.review{position:absolute;top:2448px;width:270px;height:230px;border:1px solid var(--line);border-radius:4px;padding:18px 20px;box-shadow:0 3px 10px rgba(0,0,0,.05)}
.stars{color:var(--star);font-size:17px;letter-spacing:2px}
.review h5{font-size:15px;font-weight:700;margin-top:8px}
.review p{font-size:13px;line-height:1.55;color:var(--muted);margin-top:10px}
.review .who{font-size:14px;color:var(--blue);font-weight:700;margin-top:14px}

/* contact */
.field{position:absolute;height:40px;background:var(--field);font-size:12px;color:var(--muted);padding:13px 14px;border-radius:2px}

/* footer */
.footer{position:absolute;left:0;top:3322px;width:1200px;height:422px;background:var(--navy);color:var(--white)}
.fcol{position:absolute;top:58px}
.fcol h6{font-size:19px;font-weight:700;margin-bottom:22px}
.fcol li{list-style:none;font-size:14px;margin-bottom:15px;color:#e4e9f2}
.fcol p{font-size:14px;line-height:1.55;color:#e4e9f2}
.social{display:flex;gap:14px;margin-top:22px}
.social i{display:block;width:28px;height:28px;border-radius:50%;background:var(--white)}
.social i.on{background:var(--blue-light)}
.crow{display:flex;gap:12px;align-items:flex-start;margin-bottom:22px;font-size:14px;color:#e4e9f2;line-height:1.5}
.copy{position:absolute;left:0;bottom:0;width:1200px;height:46px;border-top:1px solid rgba(255,255,255,.15);text-align:center;font-size:13px;line-height:46px;color:#cdd5e3}
</style>
</head>
<body>

<header class="hero">
  <div class="abs" role="img" aria-label="Aerial photo of a cruise ship sailing off a green tropical coast" style="inset:0"></div>
  <div class="hero-shade"></div>
  <div class="hero-ship"></div>
  <nav class="nav">
    <div class="brand"><span class="mark"></span>Floeline.co</div>
    <div class="nav-links">
      <span class="active">Home</span><span>Cruise Lines</span><span>Destinations</span><span>Itineraries</span><span>More ⌄</span>
    </div>
    <div class="nav-cta">Explore Destination</div>
  </nav>
  <h1>Your Dream Cruise Awaits</h1>
  <p>Explore breathtaking destinations, world-class ships, and unforgettable experiences. Find the perfect cruise for your next adventure!</p>
  <div class="search">
    <div class="sel">Destination <span>⌄</span></div>
    <div class="sel">Departure Date <span></span></div>
    <div class="sel">Cruise Line <span>⌄</span></div>
  </div>
  <div class="btn">Find My Cruise</div>
  <div class="play"><svg width="68" height="68" viewBox="0 0 68 68"><polygon points="28,22 28,46 48,34" fill="#fff"/></svg></div>
  <div class="dots" style="left:564px;top:640px"><i class="on"></i><i></i><i></i></div>
</header>

<section>
  <h2 class="title" style="top:770px">Featured <span>Offers</span></h2>
  <div class="sub" style="top:835px">Exclusive Cruise Deals &amp; Limited-Time Offers</div>
  <div class="arrow" style="left:58px;top:1078px"><svg width="14" height="14"><polyline points="9,2 4,7 9,12" fill="none" stroke="#fff" stroke-width="2"/></svg></div>
  <div class="arrow" style="left:1108px;top:1078px"><svg width="14" height="14"><polyline points="5,2 10,7 5,12" fill="none" stroke="#fff" stroke-width="2"/></svg></div>
  <article class="offer" style="left:120px">
    <div class="img" role="img" aria-label="Gift box with a bow on a table" style="background:linear-gradient(135deg,#5a8a4a,#c59a58 55%,#7a3d2a)"></div>
    <h3>Best Antarctic Cruises</h3>
    <p>Excepteur sint occaecat cupidatat non proident, sunt in culpa qui officia deserunt.</p>
    <div class="btn">Read More</div>
  </article>
  <article class="offer" style="left:451px">
    <div class="img" role="img" aria-label="Hands exchanging a payment card" style="background:linear-gradient(135deg,#e6dccf,#c9ad8e 50%,#8e6c4e)"></div>
    <h3>Top Galápagos Cruises</h3>
    <p>Excepteur sint occaecat cupidatat non proident, sunt in culpa qui officia deserunt.</p>
    <div class="btn">Read More</div>
  </article>
  <article class="offer" style="left:782px">
    <div class="img" role="img" aria-label="Traveller holding a passport and ticket" style="background:linear-gradient(135deg,#3c4a3c,#8a7a5c 50%,#c9b08a)"></div>
    <h3>Last-Minute Deals</h3>
    <p>Excepteur sint occaecat cupidatat non proident, sunt in culpa qui officia deserunt.</p>
    <div class="btn">Read More</div>
  </article>
</section>

<section class="dest" role="img" aria-label="Dark photo of a harbour with docked cruise ships">
  <h2 class="title">Our Destinations</h2>
  <div class="sub">Explore breathtaking destinations, world-class cruise lines, and exclusive offers. Start your journey today!</div>
  <div class="dest-item" style="left:150px">
    <div class="ic"><svg width="44" height="44" viewBox="0 0 44 44" fill="none" stroke="#fff" stroke-width="2.5"><circle cx="22" cy="22" r="18"/><ellipse cx="22" cy="22" rx="8" ry="18"/><line x1="4" y1="22" x2="40" y2="22"/></svg></div>
    <h4>Region</h4><p>Risus commodo viverra maecenas accumsan lacus vel facilisis.</p>
  </div>
  <div class="dest-item" style="left:480px">
    <div class="ic"><svg width="44" height="44" viewBox="0 0 44 44" fill="none" stroke="#fff" stroke-width="2.5"><path d="M22 40s-13-13-13-23a13 13 0 0 1 26 0c0 10-13 23-13 23z"/><circle cx="22" cy="17" r="5"/></svg></div>
    <h4>Country</h4><p>Risus commodo viverra maecenas accumsan lacus vel facilisis.</p>
  </div>
  <div class="dest-item" style="left:810px">
    <div class="ic"><svg width="44" height="44" viewBox="0 0 44 44" fill="none" stroke="#fff" stroke-width="2.5"><rect x="6" y="16" width="12" height="24"/><rect x="20" y="6" width="16" height="34"/><line x1="25" y1="14" x2="31" y2="14"/><line x1="25" y1="22" x2="31" y2="22"/><line x1="25" y1="30" x2="31" y2="30"/></svg></div>
    <h4>City</h4><p>Risus commodo viverra maecenas accumsan lacus vel facilisis.</p>
  </div>
</section>

<section>
  <h2 class="cl-title">Cruise <span>Lines</span></h2>
  <p class="cl-text">Sail with the world's top cruise lines and experience unmatched luxury, adventure, and comfort.</p>
  <div class="btn abs" style="left:112px;top:2198px;width:128px;height:36px">View All</div>
  <div class="cl-card" style="left:452px;width:240px;background:linear-gradient(180deg,#2f6fbf,#1f4f93)" role="img" aria-label="Cruise line feature card with company placeholder"></div>
  <div class="cl-card" style="left:706px;width:236px;background:linear-gradient(180deg,#7fa7c8,#3f6e5c 55%,#1f4a6a)" role="img" aria-label="Ship in a mountain fjord"></div>
  <div class="cl-card" style="left:956px;width:244px;background:linear-gradient(180deg,#cfdbe8,#eef1f4 50%,#6e8fae)" role="img" aria-label="Large white cruise ship at sea"></div>
  <div class="arrow" style="left:1050px;top:2236px;background:var(--navy)"><svg width="14" height="14"><polyline points="9,2 4,7 9,12" fill="none" stroke="#fff" stroke-width="2"/></svg></div>
  <div class="arrow" style="left:1088px;top:2236px;background:var(--navy)"><svg width="14" height="14"><polyline points="5,2 10,7 5,12" fill="none" stroke="#fff" stroke-width="2"/></svg></div>
</section>

<section>
  <h2 class="title" style="top:2372px">What Our <span>Clients Say</span></h2>
  <div class="review" style="left:112px"><div class="stars">★★★★★</div><h5>Lorem ipsum dolor</h5><p>Lorem ipsum dolor sit amet, consectetur adipiscing elit, sed do eiusmod tempor incididunt ut labore et dolore magna aliqua.</p><div class="who">Nora K</div></div>
  <div class="review" style="left:465px"><div class="stars">★★★★★</div><h5>Lorem ipsum dolor</h5><p>Lorem ipsum dolor sit amet, consectetur adipiscing elit, sed do eiusmod tempor incididunt ut labore et dolore magna aliqua.</p><div class="who">Owen T</div></div>
  <div class="review" style="left:818px"><div class="stars">★★★★★</div><h5>Lorem ipsum dolor</h5><p>Lorem ipsum dolor sit amet, consectetur adipiscing elit, sed do eiusmod tempor incididunt ut labore et dolore magna aliqua.</p><div class="who">Clara M</div></div>
  <div class="dots" style="left:564px;top:2702px"><i class="on" style="background:var(--blue)"></i><i style="background:#c9d3e2"></i><i style="background:#c9d3e2"></i></div>
</section>

<section>
  <h2 class="title" style="top:2775px">Contact <span>Us</span></h2>
  <div class="sub" style="top:2838px;left:420px;width:360px;font-size:14px;line-height:1.5">Have questions or need assistance? Fill out the form below, and our team will get back to you.</div>
  <div class="field" style="left:112px;top:2906px;width:486px">First Name</div>
  <div class="field" style="left:622px;top:2906px;width:466px">Last Name</div>
  <div class="field" style="left:112px;top:2966px;width:486px">Phone</div>
  <div class="field" style="left:622px;top:2966px;width:466px">Email</div>
  <div class="field" style="left:112px;top:3026px;width:976px;height:140px">Message</div>
  <div class="btn abs" style="left:492px;top:3196px;width:150px;height:38px">Submit</div>
  <div class="abs" style="left:660px;top:3192px;width:46px;height:46px;border-radius:50%;background:var(--green)"></div>
</section>

<footer class="footer">
  <div class="fcol" style="left:112px;width:220px">
    <h6>About Us</h6>
    <p>Excepteur sint occaecat cupidatat non proident, sunt in culpa qui officia deserunt mollit anim id est laborum.</p>
    <div class="social"><i class="on"></i><i></i><i></i><i></i></div>
  </div>
  <div class="fcol" style="left:432px">
    <h6>Main Links</h6>
    <ul><li>Home</li><li>Cruise Lines</li><li>Destinations</li><li>Itineraries</li><li>Blog/Travel Tips</li></ul>
  </div>
  <div class="fcol" style="left:668px;width:230px">
    <h6>Contact Us</h6>
    <div class="crow"><svg width="16" height="18" viewBox="0 0 16 18" fill="none" stroke="#fff" stroke-width="1.6"><path d="M8 17s-6-6-6-10a6 6 0 0 1 12 0c0 4-6 10-6 10z"/><circle cx="8" cy="7" r="2"/></svg><span>48, Floeline Cruise House<br>No. 20417</span></div>
    <div class="crow"><svg width="16" height="16" viewBox="0 0 16 16" fill="none" stroke="#fff" stroke-width="1.6"><path d="M3 1h3l1.5 4-2 1.5a9 9 0 0 0 4 4l1.5-2 4 1.5v3a1.5 1.5 0 0 1-1.5 1.5A13.5 13.5 0 0 1 1.5 2.5 1.5 1.5 0 0 1 3 1z"/></svg><span>+1 555 014 2290</span></div>
    <div class="crow"><svg width="16" height="14" viewBox="0 0 16 14" fill="none" stroke="#fff" stroke-width="1.6"><rect x="1" y="1" width="14" height="12"/><polyline points="1,1 8,8 15,1"/></svg><span>hello@floeline.co</span></div>
  </div>
  <div class="fcol" style="left:976px">
    <h6>Other Links</h6>
    <ul><li>About Us</li><li>Contact</li><li>FAQs</li><li>Privacy Policy</li><li>Terms Of Use</li></ul>
  </div>
  <div class="copy">Copyright © 2025 Floeline. All rights reserved.</div>
</footer>

</body>
</html>
```